Personal Training

Personal Fitness Trainer
Sports Nutritionist
Individual and Group rates available
Certifications
Global Wellness Coaches Federation
Worldwide Athletic Study Council

Industry/Entity Type

Fitness

Contact Information for Business Card

Dorinda Valcourt
555-284-7160
dvalcourt4@brimfeld.com

```html
<!DOCTYPE html>
<html lang="en">
<head>
<meta charset="utf-8">
<title>Dorinda Valcourt – Personal Training Business Card</title>
<link rel="stylesheet" href="https://fonts.googleapis.com/css2?family=Arimo:wght@400&family=Noto+Serif:ital,wght@1,700&display=swap">
<style>
  :root {
    --page-bg: #e9e6e2;
    --card-red: #b3222f;
    --card-wine: #7a1a34;
    --card-plum: #3b1233;
    --card-dusk: #4d3452;
    --ink-light: #ffffff;
    --photo-light: #d9d6d3;
    --photo-warm: #a4715a;
    --photo-frame: #f4f1f1;
  }
  * { margin: 0; padding: 0; box-sizing: border-box; }
  html, body {
    width: 1200px;
    height: 901px;
    overflow: hidden;
    background: var(--page-bg);
  }
  .sheet {
    position: relative;
    width: 1200px;
    height: 901px;
    display: flex;
    align-items: center;
    justify-content: center;
    gap: 40px;
  }
  .card {
    position: relative;
    width: 530px;
    height: 303px;
    border-radius: 4px;
    color: var(--ink-light);
    box-shadow: 0 10px 28px rgba(0, 0, 0, 0.22);
    overflow: hidden;
  }
  /* Back side: services */
  .card--back {
    background: linear-gradient(172deg, var(--card-red) 0%, var(--card-wine) 38%, var(--card-dusk) 100%);
    text-align: center;
    padding-top: 48px;
    font-family: "Arimo", Arial, sans-serif;
  }
  .services-title {
    font-family: "Noto Serif", Georgia, serif;
    font-style: italic;
    font-weight: 700;
    font-size: 30px;
    letter-spacing: 0.5px;
    margin-bottom: 20px;
  }
  .services-list {
    list-style: none;
    font-size: 19px;
    line-height: 23px;
  }
  /* Front side: identity */
  .card--front {
    background: linear-gradient(212deg, var(--card-red) 0%, var(--card-wine) 45%, var(--card-plum) 78%, var(--card-dusk) 100%);
    font-family: "Arimo", Arial, sans-serif;
  }
  .portrait {
    position: absolute;
    left: 60px;
    top: 16px;
    width: 250px;
    height: 164px;
  }
  .identity {
    position: absolute;
    right: 30px;
    top: 188px;
    text-align: left;
  }
  .identity__name {
    font-family: "Noto Serif", Georgia, serif;
    font-style: italic;
    font-weight: 700;
    font-size: 32px;
    line-height: 42px;
    letter-spacing: 1px;
    white-space: nowrap;
    margin-bottom: 8px;
  }
  .identity__contact {
    font-size: 18px;
    line-height: 23px;
    padding-left: 4px;
  }
</style>
</head>
<body>
  <main class="sheet">
    <section class="card card--back" aria-label="Card back: services">
      <h2 class="services-title">Services</h2>
      <ul class="services-list">
        <li>Certifications</li>
        <li>Sports Nutritionist</li>
        <li>Personal Fitness Trainer</li>
        <li>Individual and Group rates available</li>
        <li>Worldwide Athletic Study Council</li>
        <li>Global Wellness Coaches Federation</li>
      </ul>
    </section>

    <section class="card card--front" aria-label="Card front: trainer contact">
      <svg class="portrait" viewBox="0 0 250 164" role="img" aria-label="Photo of the trainer posing in athletic wear">
        <defs>
          <linearGradient id="portrait-fill" x1="0" y1="0" x2="1" y2="1">
            <stop offset="0" stop-color="var(--photo-light)"/>
            <stop offset="0.55" stop-color="var(--photo-warm)"/>
            <stop offset="1" stop-color="var(--card-plum)"/>
          </linearGradient>
        </defs>
        <ellipse cx="125" cy="82" rx="120" ry="77" fill="url(#portrait-fill)" stroke="var(--photo-frame)" stroke-width="5"/>
      </svg>
      <div class="identity">
        <h1 class="identity__name">Dorinda Valcourt</h1>
        <p class="identity__contact">555-284-7160<br>dvalcourt4@brimfeld.com</p>
      </div>
    </section>
  </main>
</body>
</html>
```